Business Card Design Project

for a second hand vintage clothing store. shop name is The Velvet Cupboard

Cards to be double sided

The name on the card is Joanna Whitfield

Information to put on card:

The Velvet Cupboard
Joanna Whitfield (no job title)
42/871 Dunmore St, Glenwick, Sydney, NSW, 2009.
Mobile: 0412 905 261
Email: thevelvetcupboard@mailbox.com.au
Web: www.thevelvetcupboard.com.au

Target Market(s)

Women looking at vintage clothing

Industry/Entity Type

Clothing

```html
<!DOCTYPE html>
<html lang="en">
<head>
<meta charset="utf-8">
<title>The Velvet Cupboard – Business Card</title>
<link rel="stylesheet" href="https://fonts.googleapis.com/css2?family=Arimo:wght@400;700&display=swap">
<style>
  :root {
    --backdrop: #f3ecdc;
    --velvet: #5e2a3a;
    --velvet-deep: #7a1f22;
    --gold-light: #fbe98a;
    --gold-mid: #f3d25a;
    --gold-deep: #e2b23a;
    --gold-name: #b98f32;
    --cream-stripe: #f6e7b4;
    --ink: #4a2420;
    --front-name: #e6c27c;
  }
  * { box-sizing: border-box; margin: 0; padding: 0; }
  html, body {
    width: 1200px;
    height: 951px;
    overflow: hidden;
    background: var(--backdrop);
    font-family: "Arimo", Arial, sans-serif;
  }
  .canvas {
    position: relative;
    width: 1200px;
    height: 951px;
  }
  .card {
    position: absolute;
    left: 280px;
    width: 640px;
    height: 366px;
    border-radius: 22px;
    overflow: hidden;
  }
  /* Front side */
  .card--front {
    top: 80px;
    background: var(--velvet);
    display: flex;
    align-items: center;
    justify-content: center;
  }
  .card--front .shop-name {
    color: var(--front-name);
    font-size: 56px;
    font-weight: 400;
    letter-spacing: 1px;
  }
  /* Back side */
  .card--back {
    top: 506px;
    background: linear-gradient(160deg, var(--gold-light) 0%, var(--gold-mid) 50%, var(--gold-deep) 100%);
    color: var(--ink);
  }
  .card__corners {
    position: absolute;
    inset: 0;
    width: 100%;
    height: 100%;
  }
  .card--back .shop-name {
    position: absolute;
    top: 58px;
    left: 0;
    width: 100%;
    text-align: center;
    color: var(--gold-name);
    font-size: 46px;
    font-weight: 400;
  }
  .holder-name {
    position: absolute;
    top: 170px;
    left: 42px;
    font-size: 24px;
    font-weight: 400;
  }
  .address {
    position: absolute;
    top: 222px;
    left: 42px;
    display: flex;
    gap: 10px;
    font-size: 15px;
    line-height: 1.3;
  }
  .contact-list {
    position: absolute;
    top: 214px;
    left: 318px;
    list-style: none;
    font-size: 15px;
  }
  .contact-list li {
    display: flex;
    align-items: center;
    gap: 10px;
    height: 25px;
  }
  .icon {
    width: 14px;
    height: 14px;
    flex: none;
    fill: var(--ink);
  }
</style>
</head>
<body>
<main class="canvas">
  <section class="card card--front" aria-label="Card front">
    <h1 class="shop-name">The Velvet Cupboard</h1>
  </section>

  <section class="card card--back" aria-label="Card back">
    <svg class="card__corners" viewBox="0 0 640 366" preserveAspectRatio="none" aria-hidden="true">
      <path d="M0 0 H110 Q40 30 0 110 Z" fill="var(--velvet-deep)"/>
      <path d="M110 0 Q40 30 0 110 V126 Q50 42 132 0 Z" fill="var(--cream-stripe)"/>
      <path d="M640 366 H540 Q610 330 640 260 Z" fill="var(--velvet-deep)"/>
      <path d="M540 366 Q610 330 640 260 V244 Q600 330 518 366 Z" fill="var(--cream-stripe)"/>
    </svg>

    <h2 class="shop-name">The Velvet Cupboard</h2>

    <p class="holder-name">Joanna Whitfield</p>

    <div class="address">
      <svg class="icon" viewBox="0 0 16 16" aria-hidden="true"><path d="M8 1 L15 8 H13 V15 H9.5 V10.5 H6.5 V15 H3 V8 H1 Z"/></svg>
      <p>42/871 Dunmore St, Glenwick,<br>Sydney, NSW, 2009.</p>
    </div>

    <ul class="contact-list">
      <li>
        <svg class="icon" viewBox="0 0 16 16" aria-hidden="true"><rect x="4" y="1" width="8" height="14" rx="1.5"/><rect x="5.5" y="3" width="5" height="7" fill="var(--gold-mid)"/></svg>
        <span>0412 905 261</span>
      </li>
      <li>
        <svg class="icon" viewBox="0 0 16 16" aria-hidden="true"><rect x="1" y="3.5" width="14" height="10" rx="1"/><path d="M1.5 4 L8 9.5 L14.5 4" fill="none" stroke="var(--gold-mid)" stroke-width="1.3"/></svg>
        <span>thevelvetcupboard@mailbox.com.au</span>
      </li>
      <li>
        <svg class="icon" viewBox="0 0 16 16" aria-hidden="true"><circle cx="8" cy="8" r="7"/></svg>
        <span>www.thevelvetcupboard.com.au</span>
      </li>
    </ul>
  </section>
</main>
</body>
</html>
```